BPH Business Card 2018

Brellmore Chiropractic. We have two locations that we want to advertise on the same card. Calderwick OrthoAxis campus address: 3815 Pemberly Dr., Suite 240, Flowood, MS 39587. Madison address: 426 Larkmoor Dr., Building D., Madison, MS 39674. website: www.drbrellmore.example. o:(601)555-0148 f:(601)555-0173

Target Market(s)

Health care decision makers: primary care doctors and mothers

Contact Information for Business Card

I have no idea; up for any suggestions and I'd do much better picking from examples versus describing what I'm looking for. We are in a very high end location and would like the cards to look really sharp.

Requirements
Must have
• My name, Tobias R Venmark, D.C.

```html
<!DOCTYPE html>
<html lang="en">
<head>
<meta charset="utf-8">
<title>Brellmore Chiropractic – Business Card</title>
<link href="https://fonts.googleapis.com/css2?family=Crimson+Text:ital,wght@0,400;0,600;1,400;1,600&display=swap" rel="stylesheet">
<style>
  :root {
    --backdrop: #ececec;
    --card-light: #fbfbfb;
    --card-dark: #2c2c2b;
    --ink: #2a2a2a;
    --ink-soft: #4a4a4a;
    --rule: #555555;
    --on-dark: #e6e6e6;
  }
  * { box-sizing: border-box; margin: 0; padding: 0; }
  html, body { width: 1200px; height: 1188px; overflow: hidden; }
  body {
    background: var(--backdrop);
    font-family: "Crimson Text", Georgia, serif;
    color: var(--ink);
    position: relative;
  }
  .card {
    position: absolute;
    left: 130px;
    width: 940px;
    height: 537px;
    box-shadow: 0 6px 18px rgba(0,0,0,0.12);
  }
  .card--front { top: 40px; background: var(--card-light); }
  .card--back { top: 611px; background: var(--card-dark); }

  .wordmark {
    text-transform: uppercase;
    font-weight: 400;
    line-height: 0.95;
    letter-spacing: 0.02em;
  }
  .wordmark span { display: block; }

  .card--front .wordmark {
    position: absolute;
    left: 110px;
    top: 62px;
    color: var(--ink);
    font-size: 58px;
  }
  .card--front .wordmark .sub { font-size: 40px; letter-spacing: 0.12em; padding-left: 4px; }

  .holder {
    position: absolute;
    left: 110px;
    top: 186px;
    width: 440px;
    font-size: 36px;
    font-weight: 600;
    color: var(--ink);
    padding-bottom: 6px;
    border-bottom: 7px solid var(--rule);
  }
  .phones {
    position: absolute;
    left: 110px;
    top: 258px;
    display: flex;
    gap: 26px;
    font-size: 24px;
    color: var(--ink-soft);
  }
  .phones .item { display: flex; align-items: center; gap: 8px; }
  .phones svg { width: 20px; height: 20px; fill: var(--ink-soft); }

  .locations {
    position: absolute;
    left: 110px;
    top: 318px;
    display: flex;
    font-size: 24px;
    line-height: 1.2;
    color: var(--ink-soft);
  }
  .location { padding-right: 34px; }
  .location + .location { padding-left: 34px; border-left: 2px solid var(--ink-soft); }
  .location .name { font-style: italic; font-weight: 600; color: var(--ink); }

  .card--back .wordmark {
    position: absolute;
    left: 0; right: 0;
    top: 170px;
    text-align: center;
    color: var(--on-dark);
    font-size: 78px;
  }
  .card--back .wordmark .sub { font-size: 54px; letter-spacing: 0.12em; }
  .website {
    position: absolute;
    left: 0; right: 0;
    top: 380px;
    text-align: center;
    color: var(--on-dark);
    font-size: 24px;
    letter-spacing: 0.04em;
  }
</style>
</head>
<body>
  <section class="card card--front" aria-label="Business card front">
    <div class="wordmark">
      <span class="main">Brellmore</span>
      <span class="sub">Chiropractic</span>
    </div>
    <div class="holder">Tobias R Venmark, D.C.</div>
    <div class="phones">
      <div class="item">
        <svg viewBox="0 0 24 24" aria-label="Phone"><path d="M6.6 10.8a15 15 0 0 0 6.6 6.6l2.2-2.2a1 1 0 0 1 1-.25 11.4 11.4 0 0 0 3.6.57 1 1 0 0 1 1 1V20a1 1 0 0 1-1 1A17 17 0 0 1 3 4a1 1 0 0 1 1-1h3.5a1 1 0 0 1 1 1c0 1.25.2 2.45.57 3.6a1 1 0 0 1-.25 1z"/></svg>
        <span>(601)555-0148</span>
      </div>
      <div class="item">
        <svg viewBox="0 0 24 24" aria-label="Fax"><path d="M7 3h8l3 3v4H7z M4 10h16a2 2 0 0 1 2 2v7a2 2 0 0 1-2 2H4a2 2 0 0 1-2-2v-7a2 2 0 0 1 2-2z"/></svg>
        <span>(601)555-0173</span>
      </div>
    </div>
    <div class="locations">
      <div class="location">
        <div class="name">Calderwick OrthoAxis Campus</div>
        <div>3815 Pemberly Dr., Suite 240</div>
        <div>Flowood, MS 39587</div>
      </div>
      <div class="location">
        <div class="name">Madison</div>
        <div>426 Larkmoor Dr., Building D.</div>
        <div>Madison, MS 39674</div>
      </div>
    </div>
  </section>

  <section class="card card--back" aria-label="Business card back">
    <div class="wordmark">
      <span class="main">Brellmore</span>
      <span class="sub">Chiropractic</span>
    </div>
    <div class="website">www.drbrellmore.example</div>
  </section>
</body>
</html>
```